Tattoostudio
Zielgruppe
Tattoostudio, Junge Leute, Kreativ,
Aufgabenstellung
Visitenkarten mit vorhandenem Logo, hochkant, 2 Seitig, Vorderseite Logo + Studioname (Morgenfalke Tattoo) Rückseite mit Kontaktdaten ( Artist/Inhaber, Facebook: facebook.com/MorgenfalkeTattoo

```html
<!DOCTYPE html>
<html lang="de">
<head>
<meta charset="utf-8">
<title>Morgenfalke Tattoo – Visitenkarten</title>
<link href="https://fonts.googleapis.com/css2?family=Libre+Baskerville:wght@400;700&display=swap" rel="stylesheet">
<style>
  :root {
    --backdrop: #5fcfbd;
    --kraft: #cdb99c;
    --kraft-dark: #b9a384;
    --ink: #3a332c;
    --ink-soft: #5a4f44;
    --frame: #4a4038;
  }
  html, body {
    margin: 0;
    padding: 0;
    width: 1200px;
    height: 818px;
    overflow: hidden;
    background: var(--backdrop);
  }
  .canvas {
    position: relative;
    width: 1200px;
    height: 818px;
    display: flex;
    justify-content: center;
    align-items: center;
    gap: 80px;
  }
  .card {
    position: relative;
    width: 380px;
    height: 600px;
    background: var(--kraft);
    box-shadow: 0 18px 40px rgba(0, 60, 50, 0.25);
    box-sizing: border-box;
  }
  .card__frame {
    position: absolute;
    inset: 16px;
    border: 1px solid var(--frame);
  }
  .card__frame::after {
    content: "";
    position: absolute;
    inset: 4px;
    border: 1.5px solid var(--frame);
  }
  .card__content {
    position: absolute;
    inset: 26px;
    display: flex;
    flex-direction: column;
    align-items: center;
  }

  /* Front */
  .front__illustration {
    margin-top: 36px;
    width: 250px;
    height: 300px;
    border-radius: 46% 46% 40% 40%;
    background: radial-gradient(circle at 55% 30%, #e9456e 0%, #7a52b8 38%, #2aa77f 62%, #e8b79c 80%, var(--kraft) 100%);
  }
  .front__name {
    margin-top: 44px;
    font-family: "Libre Baskerville", serif;
    font-weight: 400;
    font-size: 34px;
    line-height: 1.15;
    color: var(--ink);
    text-align: center;
  }

  /* Back */
  .back__content { justify-content: center; }
  .back__mark {
    width: 52px;
    height: 60px;
    border-radius: 45%;
    background: radial-gradient(circle at 50% 35%, #e9456e 0%, #7a52b8 45%, #2aa77f 70%, var(--kraft) 100%);
    margin-bottom: 14px;
  }
  .back__name {
    font-family: "Libre Baskerville", serif;
    font-weight: 700;
    font-size: 17px;
    letter-spacing: 0.06em;
    color: var(--ink);
    margin: 0 0 8px;
  }
  .back__details {
    font-family: "Libre Baskerville", serif;
    font-size: 11.5px;
    line-height: 1.55;
    color: var(--ink-soft);
    text-align: center;
    margin: 0;
  }
  .back__details .gap { display: block; height: 8px; }
</style>
</head>
<body>
<main class="canvas">
  <section class="card card--front">
    <div class="card__frame"></div>
    <div class="card__content">
      <div class="front__illustration" role="img" aria-label="Farbige Tattoo-Illustration einer Frau mit bunten Haaren, Blume und Tätowiermaschine"></div>
      <div class="front__name">Morgenfalke<br>Tattoo</div>
    </div>
  </section>

  <section class="card card--back">
    <div class="card__frame"></div>
    <div class="card__content back__content">
      <div class="back__mark" role="img" aria-label="Kleine Version der farbigen Studio-Illustration"></div>
      <h1 class="back__name">MORGENFALKE TATTOO</h1>
      <p class="back__details">
        Artist/Inhaber: Lena Brandt<br>
        Lindenweg 8,<br>
        07745 Kleinhausen<br>
        Tel.: 0170 5550123
        <span class="gap"></span>
        Email: info@morgenfalke-tattoo.de<br>
        Facebook: facebook.com/MorgenfalkeTattoo
      </p>
    </div>
  </section>
</main>
</body>
</html>
```